Business Card Design Project

Brenton
Sales Manager

38750 Harlow Ave, Suite 415
Dunmore, CA 93581

Tel: 714-382-5061
Fax: 877-524-3917
E-mail: brenton@lumobravo.com

Target Market(s)

We are the distributor and wholesaler, the business card design want to show we are a strong company.

Industry/Entity Type

Business

Colors

Designer to choose colors to be used in the design.

```html
<!DOCTYPE html>
<html lang="en">
<head>
<meta charset="utf-8">
<title>Lumobravo Business Card</title>
<link href="https://fonts.googleapis.com/css2?family=Open+Sans:wght@400;600&display=swap" rel="stylesheet">
<style>
  :root {
    --page-bg: #e6e6e8;
    --card-white: #ffffff;
    --brand-red: #e8321e;
    --brand-orange: #f26a10;
    --brand-amber: #ffab0a;
    --soft-grey: #ececec;
    --text-red: #e23a26;
  }
  * { box-sizing: border-box; margin: 0; padding: 0; }
  html, body { width: 1200px; height: 873px; overflow: hidden; }
  body {
    background: var(--page-bg);
    font-family: "Open Sans", Arial, sans-serif;
    position: relative;
  }
  .card {
    position: absolute;
    top: 286px;
    width: 520px;
    height: 300px;
    border-radius: 4px;
    box-shadow: 0 6px 18px rgba(0,0,0,.18);
    overflow: hidden;
  }
  .card-front { left: 50px; background: var(--card-white); }
  .card-back {
    left: 630px;
    background: linear-gradient(125deg, var(--brand-red) 0%, var(--brand-orange) 45%, var(--brand-amber) 100%);
    display: flex; align-items: center; justify-content: center;
  }
  .brand-disc {
    position: absolute;
    left: 32px; top: 50px;
    width: 200px; height: 200px;
    border-radius: 50%;
    background: var(--soft-grey);
    display: flex; align-items: center; justify-content: center;
  }
  .brand-name {
    font-weight: 600;
    font-size: 27px;
    color: var(--brand-red);
    letter-spacing: .5px;
  }
  .card-back .brand-name { color: var(--card-white); font-size: 40px; }
  .divider {
    position: absolute;
    left: 262px; top: 40px;
    width: 2px; height: 220px;
    background: linear-gradient(to bottom, var(--brand-red), var(--brand-amber));
  }
  .contact {
    position: absolute;
    left: 288px; top: 54px;
    color: var(--text-red);
  }
  .person-name { font-size: 36px; line-height: 1; font-weight: 400; }
  .person-title { font-size: 14px; color: var(--brand-orange); margin: 6px 0 20px; }
  .contact-row {
    display: flex; align-items: flex-start; gap: 10px;
    font-size: 12.5px; line-height: 18px;
    margin-bottom: 4px;
  }
  .contact-row svg { flex: none; width: 13px; height: 13px; margin-top: 3px; }
</style>
</head>
<body>
  <section class="card card-front">
    <div class="brand-disc"><span class="brand-name">Lumobravo</span></div>
    <div class="divider"></div>
    <div class="contact">
      <h1 class="person-name">Brenton</h1>
      <p class="person-title">Sales Manager</p>
      <div class="contact-row">
        <svg viewBox="0 0 12 12" fill="none" stroke="currentColor" stroke-width="1.3"><path d="M6 11s4-4 4-6.5A4 4 0 0 0 2 4.5C2 7 6 11 6 11z"/><circle cx="6" cy="4.6" r="1.4"/></svg>
        <span>38750 Harlow Ave, Suite 415<br>Dunmore, CA 93581</span>
      </div>
      <div class="contact-row">
        <svg viewBox="0 0 12 12" fill="none" stroke="currentColor" stroke-width="1.3"><rect x="3" y="1" width="6" height="10" rx="1"/><path d="M5.2 9.3h1.6"/></svg>
        <span>714-382-5061</span>
      </div>
      <div class="contact-row">
        <svg viewBox="0 0 12 12" fill="none" stroke="currentColor" stroke-width="1.3"><rect x="1.5" y="4.5" width="9" height="5" rx=".6"/><path d="M3.5 4.5V1.5h5v3M3.5 9.5v1.5h5V9.5"/></svg>
        <span>877-524-3917</span>
      </div>
      <div class="contact-row">
        <svg viewBox="0 0 12 12" fill="none" stroke="currentColor" stroke-width="1.3"><rect x="1" y="2.5" width="10" height="7" rx=".6"/><path d="M1 3l5 3.5L11 3"/></svg>
        <span>brenton@lumobravo.com</span>
      </div>
    </div>
  </section>

  <section class="card card-back">
    <span class="brand-name">Lumobravo</span>
  </section>
</body>
</html>
```